Sports medicine multidisciplinary brochures

Multi-disciplinary sports medicine clinic. Need a range of pamphlet / foldable brochures to advertise our various services. Looking at keeping a similar 'look' between the various brochures to still ID as being part of the group, but perhaps slight colour variation / different front pic to distinguish them. Looking at a pamphlet for: 1) General clinic (about us) info 2) Concussion info 3) Podiatry 4) Sports Physicians 5) Exercise Physiology 6) Osteoarthritis 7) Physiotherapy. Modern feel, but still warm / inviting. See attached logo / cards / etc. Thank you!

Target Market(s)

Athletes, sports injuries + general health / medical

Industry/Entity Type

Clinic

Requirements
Nice to have
• Simple, warm design. Activity / health / lifestyle related feel.
• Design to allow easy adaptation of wording / content.

```html
<!DOCTYPE html>
<html lang="en">
<head>
<meta charset="utf-8">
<title>Stride &amp; Joint Clinic – Brochure Covers</title>
<link rel="stylesheet" href="https://fonts.googleapis.com/css2?family=Lato:wght@400;700;900&family=Oswald:wght@500;700&display=swap">
<style>
  :root {
    --orange: #f26b0f;
    --orange-light: #ff8f1f;
    --green: #239a5c;
    --dark: #2e2a2b;
    --paper: #f4f4f4;
    --paper-shade: #e2e2e2;
    --ink: #1e1e1e;
    --page-bg: #d9d9d9;
  }
  html, body {
    margin: 0;
    padding: 0;
    width: 1200px;
    height: 1200px;
    overflow: hidden;
    background: var(--page-bg);
  }
  .brochure-spread {
    position: absolute;
    left: 140px;
    top: 275px;
    width: 920px;
    height: 650px;
    box-shadow: 0 14px 40px rgba(0,0,0,0.25);
  }
  .brochure-spread svg { display: block; }
  .paper { fill: var(--paper); }
  .orange-fill { fill: var(--orange); }
  .green-fill { fill: var(--green); }
  .dark-fill { fill: var(--dark); }
  .orange-line { fill: none; stroke: var(--orange); }
  .green-line { fill: none; stroke: var(--green); }
  .intro-text {
    font-family: 'Lato', sans-serif;
    font-size: 12.5px;
    fill: #ffffff;
  }
  .contact-heading {
    font-family: 'Oswald', sans-serif;
    font-weight: 700;
    font-size: 22px;
    fill: var(--green);
    letter-spacing: 0.5px;
  }
  .contact-text {
    font-family: 'Lato', sans-serif;
    font-weight: 700;
    font-size: 14px;
    fill: var(--ink);
  }
  .brand-name {
    font-family: 'Lato', sans-serif;
    font-weight: 900;
    font-size: 40px;
    fill: var(--green);
    letter-spacing: 4px;
  }
  .title-dark {
    font-family: 'Oswald', sans-serif;
    font-weight: 700;
    font-size: 66px;
    fill: var(--dark);
  }
  .title-green {
    font-family: 'Oswald', sans-serif;
    font-weight: 700;
    font-size: 40px;
    fill: var(--green);
  }
  .fold-shade { fill: url(#foldShade); }
</style>
</head>
<body>
<div class="brochure-spread">
  <svg width="920" height="650" viewBox="0 0 920 650" xmlns="http://www.w3.org/2000/svg">
    <defs>
      <linearGradient id="orangeWash" x1="0" y1="0" x2="1" y2="1">
        <stop offset="0" stop-color="#ff9a26"/>
        <stop offset="1" stop-color="#f0600c"/>
      </linearGradient>
      <linearGradient id="foldShade" x1="0" y1="0" x2="1" y2="0">
        <stop offset="0" stop-color="#000" stop-opacity="0"/>
        <stop offset="0.5" stop-color="#000" stop-opacity="0.08"/>
        <stop offset="1" stop-color="#000" stop-opacity="0"/>
      </linearGradient>
      <linearGradient id="photoKnee" x1="0" y1="0" x2="1" y2="1">
        <stop offset="0" stop-color="#f3f6fa"/>
        <stop offset="0.5" stop-color="#e8c3a6"/>
        <stop offset="1" stop-color="#9fc0de"/>
      </linearGradient>
      <linearGradient id="photoNeck" x1="0" y1="0" x2="1" y2="1">
        <stop offset="0" stop-color="#8a8784"/>
        <stop offset="0.55" stop-color="#e6c2a8"/>
        <stop offset="1" stop-color="#f7f7f7"/>
      </linearGradient>
      <linearGradient id="photoBand" x1="0" y1="0" x2="1" y2="1">
        <stop offset="0" stop-color="#f5f5f5"/>
        <stop offset="0.5" stop-color="#e9c7ae"/>
        <stop offset="1" stop-color="#3fae7a"/>
      </linearGradient>
    </defs>

    <!-- Back cover -->
    <g class="back-cover">
      <rect class="paper" x="0" y="0" width="460" height="650"/>
      <path d="M0,0 H460 V150 C400,210 300,250 250,255 L252,232 L215,262 C140,280 60,320 0,365 Z" fill="url(#orangeWash)"/>
      <path class="green-line" stroke-width="5" d="M460,150 C400,210 300,250 250,255 L252,232 L215,262 C140,280 60,320 0,365"/>
      <text class="intro-text">
        <tspan x="40" y="48">Stride and Joint Clinic is a new multidisciplinary clinic</tspan>
        <tspan x="40" y="64">with specialist sports and exercise physicians as the</tspan>
        <tspan x="40" y="80">leads. It is unique in Westfield, aiming to provide</tspan>
        <tspan x="40" y="96">affordable, evidence based, non-surgical treatment for</tspan>
        <tspan x="40" y="112">sport and musculoskeletal injuries, as well as arthritis.</tspan>
        <tspan x="40" y="140">Combining specialist physician care with select</tspan>
        <tspan x="40" y="156">physiotherapists, podiatry and other allied health,</tspan>
        <tspan x="40" y="172">integrated with our new fully equipped gym and</tspan>
        <tspan x="40" y="188">modern software, we are well placed to work with you.</tspan>
      </text>
      <text class="contact-heading" x="230" y="420" text-anchor="middle">CONTACT DETAILS</text>
      <text class="contact-text" text-anchor="middle">
        <tspan x="230" y="450">Stride and Joint Clinic</tspan>
        <tspan x="230" y="470">14 Harbour View Rd, Westfield 5040</tspan>
        <tspan x="230" y="500">Telephone 08 5550 1234</tspan>
        <tspan x="230" y="530">info@stridejoint.example</tspan>
        <tspan x="230" y="550">www.stridejointclinic.example</tspan>
      </text>
      <rect class="green-fill" x="0" y="628" width="460" height="22"/>
    </g>

    <!-- Front cover -->
    <g class="front-cover">
      <rect class="paper" x="460" y="0" width="460" height="650"/>
      <path class="dark-fill" d="M470,0 H920 V470 C880,400 820,380 760,360 C650,320 620,220 560,140 C520,90 500,40 470,0 Z"/>
      <path class="orange-line" stroke-width="6" d="M470,0 C500,40 520,90 560,140 C620,220 650,320 760,360 C820,380 880,400 920,470"/>

      <g role="img" aria-label="Photo: physiotherapist treating a patient's neck and shoulders">
        <circle cx="810" cy="180" r="112" fill="url(#photoNeck)"/>
        <circle class="green-line" cx="810" cy="180" r="112" stroke-width="9"/>
      </g>
      <g role="img" aria-label="Photo: clinician examining a patient's knee">
        <circle cx="640" cy="215" r="98" fill="url(#photoKnee)"/>
        <circle class="orange-line" cx="640" cy="215" r="98" stroke-width="8"/>
      </g>
      <g role="img" aria-label="Photo: patient doing resistance band exercise with a therapist">
        <circle cx="745" cy="340" r="68" fill="url(#photoBand)"/>
        <circle class="orange-line" cx="745" cy="340" r="68" stroke-width="7"/>
      </g>

      <g class="brand-mark">
        <circle class="orange-fill" cx="588" cy="425" r="14"/>
        <text class="brand-name" x="612" y="440">STRIDE</text>
      </g>

      <g class="cover-title">
        <text class="title-dark" x="900" y="520" text-anchor="end">STRIDE</text>
        <text class="title-green" x="900" y="565" text-anchor="end">&amp; JOINT</text>
        <text class="title-dark" x="900" y="628" text-anchor="end">CLINIC</text>
      </g>

      <rect class="orange-fill" x="460" y="636" width="460" height="14"/>
    </g>

    <rect class="fold-shade" x="430" y="0" width="60" height="650"/>
  </svg>
</div>
</body>
</html>
```